Business Card design for construction company

I would like a business card design for a construction company - Harlow Constructions. I have attached the ai logo file for use. I would like the card to be very smart and clean and incorporate only white and the two colours in the logo. I would like the card to have two sides. One side can just have the logo, the other with the relevant information.

Target Market(s)

Building and Construction Clients

Industry/Entity Type

Business

Contact Information for Business Card

Name: Tom Pardoe
Company: Harlow Constructions Pty Limited
Address: 14 Mallee Crescent Carrow Vale 2093
Phone: 0427 531 068
Email: tomp@harlowbuild-example.com.au

Font styles to use
Serif
Sans Serif

Requirements
Must have
• Details noted above
• Logo as provided
• Colours as in logo
• Square edges
• A font that compliments the logo
Should not have
• Any colour other than white and those in logo
• Rounded edges

```html
<!DOCTYPE html>
<html lang="en">
<head>
<meta charset="utf-8">
<title>Harlow Constructions – Business Cards</title>
<link rel="stylesheet" href="https://fonts.googleapis.com/css2?family=Montserrat:wght@400;600;700&family=Open+Sans:wdth,wght@75,400&display=swap">
<style>
  :root {
    --bg: #d9dcdf;
    --card: #ffffff;
    --ink: #555658;
    --accent: #1aa9e1;
  }
  * { margin: 0; padding: 0; box-sizing: border-box; }
  html, body { width: 1200px; height: 847px; overflow: hidden; background: var(--bg); }
  .board { position: relative; width: 1200px; height: 847px; }
  .card {
    position: absolute; width: 504px; height: 308px;
    background: var(--card);
    box-shadow: 0 1px 5px rgba(0,0,0,0.12);
  }
  .card--front-a { left: 77px; top: 77px; }
  .card--back-a  { left: 619px; top: 77px; }
  .card--front-b { left: 77px; top: 462px; }
  .card--back-b  { left: 619px; top: 462px; }

  .wordmark {
    position: absolute; display: flex; align-items: center; gap: 10px;
    font-family: "Montserrat", sans-serif; font-weight: 400;
    color: var(--ink); letter-spacing: 2.5px; white-space: nowrap;
  }
  .wordmark__dot { width: 7px; height: 7px; background: var(--accent); flex: none; }
  .card--front-a .wordmark { left: 50%; top: 154px; transform: translate(-50%, -50%); font-size: 18px; }
  .card--front-b .wordmark { right: 19px; top: 265px; transform: translateY(-50%); font-size: 16px; }

  .holder { position: absolute; text-align: right; white-space: nowrap; }
  .holder__name {
    font-family: "Montserrat", sans-serif; font-weight: 600;
    color: var(--accent); font-size: 18px; letter-spacing: 0.3px; line-height: 22px;
  }
  .holder__company {
    font-family: "Open Sans", sans-serif; font-stretch: 75%;
    color: var(--ink); font-size: 14px; line-height: 18px;
  }
  .rule { position: absolute; width: 2px; background: var(--accent); }

  .contacts { position: absolute; list-style: none; white-space: nowrap; }
  .contacts li {
    font-family: "Open Sans", sans-serif; font-stretch: 75%;
    color: var(--ink); font-size: 14px; line-height: 21.6px;
  }
  .contacts__label {
    font-family: "Montserrat", sans-serif; font-weight: 700;
    font-size: 12.5px; margin-right: 4px;
  }
  .contacts__label i { font-style: normal; color: var(--accent); }

  .card--back-a .holder { right: 299px; top: 141px; }
  .card--back-a .rule { left: 220px; top: 115px; height: 83px; }
  .card--back-a .contacts { left: 236px; top: 124px; }

  .card--back-b .holder { right: 273px; top: 33px; }
  .card--back-b .rule { left: 247px; top: 19px; height: 271px; }
  .card--back-b .contacts { left: 262px; top: 217px; }
</style>
</head>
<body>
<main class="board">
  <section class="card card--front-a">
    <div class="wordmark"><span class="wordmark__dot"></span>HARLOW CONSTRUCTIONS</div>
  </section>

  <section class="card card--back-a">
    <div class="holder">
      <p class="holder__name">TOM PARDOE</p>
      <p class="holder__company">Harlow Constructions Pty Limited</p>
    </div>
    <div class="rule"></div>
    <ul class="contacts">
      <li><span class="contacts__label">E<i>.</i></span> tomp@harlowbuild-example.com.au</li>
      <li><span class="contacts__label">P<i>.</i></span> 0427 531 068</li>
      <li><span class="contacts__label">A<i>.</i></span> 14 Mallee Crescent Carrow Vale 2093</li>
    </ul>
  </section>

  <section class="card card--front-b">
    <div class="wordmark"><span class="wordmark__dot"></span>HARLOW CONSTRUCTIONS</div>
  </section>

  <section class="card card--back-b">
    <div class="holder">
      <p class="holder__name">TOM PARDOE</p>
      <p class="holder__company">Harlow Constructions Pty Limited</p>
    </div>
    <div class="rule"></div>
    <ul class="contacts">
      <li><span class="contacts__label">E<i>.</i></span> tomp@harlowbuild-example.com.au</li>
      <li><span class="contacts__label">P<i>.</i></span> 0427 531 068</li>
      <li><span class="contacts__label">A<i>.</i></span> 14 Mallee Crescent Carrow Vale 2093</li>
    </ul>
  </section>
</main>
</body>
</html>
```